Business Card Design Project

This is to go hand in hand with our stationery project.
Target Market(s)
Business Professionals in the Finance, HR and C-Level management arena. They are global companies that run enterprise technology solutions/products.
Mostly Male, mid 30's to 60's.
Industry/Entity Type
Business
Font styles to use
Other font styles liked:
- Calibri
Colors
9bcb3c
000000
1b1b1b
c4c4c4
ffffff
Requirements
Must have
- Logo
Name, title, contact details, address on the front of the card.
ABN and web address need to be on the card, along with our tag line
See | Share | Do
We also require rounded corners and for the card to be landscape please.
Our green is
C98 M0 Y93 K0
Modern, contemporary and must have white space for people to write on.
Nice to have
- Consistent elements with the stationery design.
Should not have
- No 90's waves - We want the feeling of movement but no wavey lines.

```html
<!DOCTYPE html>
<html lang="en">
<head>
<meta charset="utf-8">
<title>Nuvra Business Solutions – Business Cards</title>
<link href="https://fonts.googleapis.com/css2?family=Carlito:wght@400;700&display=swap" rel="stylesheet">
<style>
  :root {
    --green: #9bcb3c;
    --green-deep: #8cbf2c;
    --black: #000000;
    --charcoal: #1b1b1b;
    --graphite: #2e2e2e;
    --silver: #c4c4c4;
    --white: #ffffff;
    --page: #ececec;
  }
  * { margin: 0; padding: 0; box-sizing: border-box; }
  html, body {
    width: 1200px; height: 1000px; overflow: hidden;
    background: var(--page);
    font-family: "Carlito", "Calibri", sans-serif;
  }
  .sheet {
    width: 1200px; height: 1000px;
    display: flex; flex-direction: column;
    align-items: center; justify-content: center; gap: 60px;
  }
  .card {
    position: relative;
    width: 700px; height: 400px;
    border-radius: 22px;
    overflow: hidden;
    box-shadow: 0 12px 30px rgba(0,0,0,0.18);
  }

  /* Back of card */
  .card--back { background: var(--green); }
  .card--back .green-field {
    position: absolute; inset: 0 0 120px 0;
    background: linear-gradient(160deg, #a8d54d 0%, var(--green) 45%, var(--green-deep) 100%);
  }
  .card--back .dark-band {
    position: absolute; left: 0; right: 0; bottom: 0; height: 120px;
    background: linear-gradient(180deg, var(--graphite) 0%, var(--charcoal) 100%);
  }
  .card--back .brand {
    position: absolute; top: 70px; left: 0; right: 0;
    justify-content: center;
  }
  .card--back .tagline {
    position: absolute; top: 170px; left: 0; right: 0;
    text-align: center;
    font-size: 46px; font-weight: 700; letter-spacing: 1px;
    color: #eef6e0;
  }
  .card--back .website {
    position: absolute; right: 48px; bottom: 46px;
    font-size: 20px; color: var(--white); letter-spacing: 0.5px;
  }

  /* Brand name */
  .brand { display: flex; align-items: center; gap: 10px; }
  .brand__dot { width: 14px; height: 14px; border-radius: 50%; flex: none; }
  .brand__name { font-weight: 700; font-size: 30px; line-height: 1.1; color: var(--white); }
  .brand__sub { font-size: 15px; color: var(--white); display: block; font-weight: 700; }
  .card--back .brand__dot { background: var(--charcoal); }
  .card--front .brand__dot { background: var(--green); }

  /* Front of card */
  .card--front {
    background: linear-gradient(125deg, #3a3a3a 0%, var(--graphite) 30%, var(--charcoal) 75%, #111 100%);
  }
  .card--front .brand {
    position: absolute; left: 48px; bottom: 70px;
  }
  .person { position: absolute; left: 330px; top: 80px; }
  .person__name {
    font-size: 50px; font-weight: 700; color: var(--green); line-height: 1;
  }
  .person__title {
    margin-top: 6px;
    font-size: 22px; color: var(--silver); letter-spacing: 0.5px;
  }
  .contact {
    position: absolute; left: 410px; top: 215px;
    list-style: none;
    font-size: 17px; line-height: 1.35; color: #e2e2e2;
  }
  .contact__label { color: var(--green); font-weight: 700; margin-right: 4px; }
</style>
</head>
<body>
  <main class="sheet">
    <section class="card card--back" aria-label="Card back">
      <div class="green-field"></div>
      <div class="dark-band"></div>
      <div class="brand">
        <span class="brand__dot"></span>
        <span class="brand__name">Nuvra<span class="brand__sub">Business Solutions</span></span>
      </div>
      <p class="tagline">Plan . Build . Grow</p>
      <p class="website">www.nuvrabusiness.com</p>
    </section>

    <section class="card card--front" aria-label="Card front">
      <div class="person">
        <h1 class="person__name">YOUR NAME</h1>
        <p class="person__title">YOUR TITTLE</p>
      </div>
      <ul class="contact">
        <li>LEVEL 7, 42 HARBOUR STREET,</li>
        <li>EASTWOOD NSW 2122</li>
        <li><span class="contact__label">T</span>+61 2 5550 1234</li>
        <li><span class="contact__label">F</span>+61 2 5550 5678</li>
        <li><span class="contact__label">ABN</span>12 345 678 901</li>
      </ul>
      <div class="brand">
        <span class="brand__dot"></span>
        <span class="brand__name">Nuvra<span class="brand__sub">Business Solutions</span></span>
      </div>
    </section>
  </main>
</body>
</html>
```